Vesit cards for web development company

We need a business card design for our company. The company develops online platforms and conducts marketing consulting. Company logo. The cards must fit in with us (a junior start UP), but they must also be professional enough to impress with investors like banks. We wish you a combination of classic and modern design

Target Market(s)

Business partners and IT and marketing customers

Industry/Entity Type

It Company

Contact Information for Business Card

Folgende Information müssen Drauf.
Name, Position, Telefon Nr., Mobile Nr., E-Mail adresse, Optional sind noch Webadresse und HRB Nummer

Colors

Designer to choose colors to be used in the design.

Requirements
Must have
• The cards have to fit into the logo later and have to be dynamic and serious at the same time

```html
<!DOCTYPE html>
<html lang="en">
<head>
<meta charset="UTF-8">
<title>Kora Development – Business Card</title>
<link href="https://fonts.googleapis.com/css2?family=Jost:wght@500;600&family=Open+Sans:wght@400&display=swap" rel="stylesheet">
<style>
  :root {
    --page-bg: #e4e4e4;
    --card-white: #ffffff;
    --brand-blue: #1573bd;
    --text-grey: #8a8a8a;
    --dash-grey: #555555;
  }
  * { box-sizing: border-box; margin: 0; padding: 0; }
  html, body {
    width: 1200px;
    height: 1000px;
    overflow: hidden;
    background: var(--page-bg);
  }
  .card {
    position: absolute;
    left: 152px;
    top: 248px;
    width: 896px;
    height: 504px;
    background: var(--card-white);
    box-shadow: 0 6px 24px rgba(0,0,0,0.12);
    overflow: hidden;
  }
  .brand {
    position: absolute;
    left: 26px;
    top: 44px;
    display: flex;
    align-items: center;
    gap: 12px;
  }
  .brand-dot {
    width: 34px;
    height: 34px;
    border-radius: 50%;
    background: var(--brand-blue);
  }
  .brand-name {
    font-family: "Jost", sans-serif;
    font-weight: 600;
    font-size: 34px;
    letter-spacing: 0.5px;
    color: var(--brand-blue);
    line-height: 1;
  }
  .identity {
    position: absolute;
    left: 76px;
    top: 246px;
    text-align: right;
  }
  .person-name {
    font-family: "Jost", sans-serif;
    font-weight: 600;
    font-size: 48px;
    letter-spacing: 0.5px;
    color: var(--brand-blue);
    line-height: 1;
  }
  .person-role {
    font-family: "Open Sans", sans-serif;
    font-size: 20px;
    color: var(--text-grey);
    line-height: 1;
    margin-top: 2px;
  }
  .contact-panel {
    position: absolute;
    left: 547px;
    top: 0;
    width: 349px;
    height: 504px;
    background: var(--brand-blue);
  }
  .panel-band {
    position: absolute;
    left: 0;
    top: 246px;
    width: 100%;
    height: 20px;
    background: var(--card-white);
  }
  .contact-box {
    position: absolute;
    left: 27px;
    top: 34px;
    width: 288px;
    height: 432px;
    background: var(--card-white);
    padding: 10px;
  }
  .contact-frame {
    width: 100%;
    height: 100%;
    border: 2px dashed var(--dash-grey);
    display: flex;
    flex-direction: column;
    justify-content: space-around;
    align-items: center;
    padding: 14px 0;
  }
  .contact-item {
    display: flex;
    flex-direction: column;
    align-items: center;
    gap: 14px;
  }
  .contact-icon { width: 26px; height: 26px; display: block; }
  .contact-text {
    font-family: "Open Sans", sans-serif;
    font-size: 17px;
    color: var(--text-grey);
    line-height: 1;
  }
</style>
</head>
<body>
  <div class="card">
    <div class="brand">
      <span class="brand-dot"></span>
      <span class="brand-name">KORA DEVELOPMENT</span>
    </div>

    <div class="identity">
      <p class="person-name">R.K MALLORY</p>
      <p class="person-role">Senior Developer</p>
    </div>

    <div class="contact-panel">
      <div class="panel-band"></div>
      <div class="contact-box">
        <div class="contact-frame">
          <div class="contact-item">
            <svg class="contact-icon" viewBox="0 0 26 26" aria-hidden="true">
              <rect x="8" y="2" width="10" height="20" rx="1.5" fill="none" stroke="var(--brand-blue)" stroke-width="2"/>
              <line x1="11.5" y1="19" x2="14.5" y2="19" stroke="var(--brand-blue)" stroke-width="1.5"/>
            </svg>
            <span class="contact-text">+805-5550142</span>
          </div>
          <div class="contact-item">
            <svg class="contact-icon" viewBox="0 0 26 26" aria-hidden="true">
              <rect x="2" y="5" width="22" height="16" fill="none" stroke="var(--brand-blue)" stroke-width="2.4"/>
              <polyline points="3,6 13,15 23,6" fill="none" stroke="var(--brand-blue)" stroke-width="2.4"/>
            </svg>
            <span class="contact-text">hello@koradev.io</span>
          </div>
          <div class="contact-item">
            <svg class="contact-icon" viewBox="0 0 26 26" aria-hidden="true">
              <circle cx="13" cy="13" r="10" fill="none" stroke="var(--brand-blue)" stroke-width="2"/>
              <ellipse cx="13" cy="13" rx="4.5" ry="10" fill="none" stroke="var(--brand-blue)" stroke-width="1.5"/>
              <line x1="3" y1="13" x2="23" y2="13" stroke="var(--brand-blue)" stroke-width="1.5"/>
              <line x1="5" y1="8" x2="21" y2="8" stroke="var(--brand-blue)" stroke-width="1.2"/>
              <line x1="5" y1="18" x2="21" y2="18" stroke="var(--brand-blue)" stroke-width="1.2"/>
            </svg>
            <span class="contact-text">koradev.io</span>
          </div>
          <div class="contact-item">
            <svg class="contact-icon" viewBox="0 0 26 26" aria-hidden="true">
              <rect x="1" y="5" width="24" height="16" fill="var(--brand-blue)"/>
              <text x="13" y="17" text-anchor="middle" font-family="Open Sans, sans-serif" font-size="10" fill="#ffffff">123</text>
            </svg>
            <span class="contact-text">5005-4470312</span>
          </div>
        </div>
      </div>
    </div>
  </div>
</body>
</html>
```